Beer Can Label named: ZAP Ginger Beer

We need a funky design for a Ginger Beer that is made from all natural ingredients. The label needs to be full of Colour, emphasis on the Ginger Root. ZAP (Zested And Poured)

Target Market(s)

None beer drinkers'

Requirements
Must have
• Name on the label must beer easy to read. Needs to be very colourful, playful & even a bit cheaky.
Nice to have
• A label that looks at the benefits of Ginger for the body in a fun artistic design.
Should not have
• Should NOT be a simple, basic, minimalistic design

```html
<!DOCTYPE html>
<html lang="en">
<head>
<meta charset="utf-8">
<title>ZAP Ginger Beer – Can Label</title>
<link rel="stylesheet" href="https://fonts.googleapis.com/css2?family=Abril+Fatface&family=Bitter:wght@700&display=swap">
<style>
  :root {
    --leaf-green: #7ed321;
    --lime-green: #a6e35a;
    --bright-green: #8fe040;
    --chilli-red: #e3161b;
    --ginger-tan: #e8b878;
    --lemon-yellow: #f5f019;
    --label-yellow: #f9f40f;
    --pale-sage: #dfe3c8;
    --ink-brown: #2b2622;
    --panel-brown: #2e2925;
    --ginger-gold: #d2b07c;
    --white: #ffffff;
    --root-light: #d4b68a;
    --root-dark: #8b6b42;
  }
  html, body {
    margin: 0;
    padding: 0;
    width: 1200px;
    height: 834px;
    overflow: hidden;
    background: var(--leaf-green);
  }
  .can-label {
    display: block;
    width: 1200px;
    height: 834px;
  }
  .brand-name {
    font-family: "Abril Fatface", serif;
    font-size: 205px;
    fill: var(--ink-brown);
  }
  .brand-tagline {
    font-family: "Bitter", serif;
    font-weight: 700;
    font-size: 34px;
    fill: var(--ink-brown);
  }
  .flavour-word {
    font-family: "Abril Fatface", serif;
    font-size: 88px;
    fill: var(--ginger-gold);
  }
  .product-word {
    font-family: "Abril Fatface", serif;
    font-size: 116px;
    fill: var(--white);
    letter-spacing: 2px;
  }
  .sparkle-dash {
    stroke: var(--ginger-gold);
    stroke-width: 6;
    stroke-linecap: round;
  }
</style>
</head>
<body>
<svg class="can-label" viewBox="0 0 1200 834" xmlns="http://www.w3.org/2000/svg">
  <defs>
    <linearGradient id="root-tone" x1="0" y1="0" x2="0" y2="1">
      <stop offset="0" stop-color="var(--root-light)"/>
      <stop offset="1" stop-color="var(--root-dark)"/>
    </linearGradient>
    <path id="tagline-curve" d="M350 590 Q600 515 855 590"/>
  </defs>

  <g class="colour-bands">
    <rect width="1200" height="834" fill="var(--leaf-green)"/>
    <polygon points="0,0 700,0 0,500" fill="var(--lime-green)"/>
    <polygon points="800,0 1200,0 1200,300 1000,420" fill="var(--chilli-red)"/>
    <polygon points="1000,420 1200,300 1200,560 1030,600" fill="var(--ginger-tan)"/>
    <polygon points="0,380 320,320 320,560 0,600" fill="var(--lemon-yellow)"/>
    <polygon points="0,600 320,560 340,760 0,834" fill="var(--pale-sage)"/>
    <polygon points="0,780 1200,720 1200,834 0,834" fill="var(--bright-green)"/>
  </g>

  <g class="mascot" role="img" aria-label="Cartoon ginger root mascot peeking over the name">
    <path d="M455 300 C420 240 450 170 520 160 C540 90 600 50 640 90 C700 80 760 130 740 190 C800 210 800 290 760 310 Z"
          fill="var(--label-yellow)"/>
    <path d="M470 296 C440 245 465 185 528 175 C548 110 598 75 636 108 C690 100 740 140 722 195 C775 215 778 280 745 300 Z"
          fill="url(#root-tone)"/>
  </g>

  <g class="name-panel">
    <rect x="330" y="282" width="540" height="320" rx="46" fill="var(--label-yellow)" stroke="var(--white)" stroke-width="6"/>
    <text class="brand-name" x="600" y="480" text-anchor="middle">ZAP</text>
    <text class="brand-tagline">
      <textPath href="#tagline-curve" startOffset="50%" text-anchor="middle">Zested And Poured</textPath>
    </text>
  </g>

  <g class="product-panel">
    <path d="M380 604 Q600 580 820 604 Q850 609 852 644 L860 764 Q860 816 805 816 L395 816 Q340 816 340 764 L350 644 Q352 609 380 604 Z"
          fill="var(--panel-brown)" stroke="var(--white)" stroke-width="6"/>
    <line class="sparkle-dash" x1="405" y1="660" x2="435" y2="665"/>
    <line class="sparkle-dash" x1="410" y1="690" x2="437" y2="684"/>
    <line class="sparkle-dash" x1="765" y1="665" x2="795" y2="660"/>
    <line class="sparkle-dash" x1="763" y1="684" x2="790" y2="690"/>
    <text class="flavour-word" x="600" y="690" text-anchor="middle">Ginger</text>
    <text class="product-word" x="600" y="800" text-anchor="middle">BEER</text>
  </g>
</svg>
</body>
</html>
```